Plakat für Verein
Zielgruppe
Wir möchten eine Veranstaltung für unseren Verein - Hinterkalmbacher Heimatpflegeverein machen.
Aufgabenstellung
Die Party der Golden 20er
Glanz-Glamour-Lebenslust
Tanzen wie früher - Feiern wie nie
21. März - Uhrzeit: 20.30 im Saal KM
Live mit DJaneMarlies
Dresscode: Goldene 20er - Fransen, Federn, Hosenträger, Zylinder
Farbe: Gold/Schgwarz

```html
<!DOCTYPE html>
<html lang="de">
<head>
<meta charset="utf-8">
<title>Die Party der Goldenen 20er – Hinterkalmbacher Heimatpflegeverein</title>
<link href="https://fonts.googleapis.com/css2?family=Limelight&family=Bitter:wght@400;500&display=swap" rel="stylesheet">
<style>
  :root {
    --black: #000000;
    --gold: #c9a860;
    --gold-light: #f2d68a;
    --gold-dark: #a88a4e;
  }
  html, body {
    margin: 0;
    padding: 0;
    width: 1200px;
    height: 520px;
    overflow: hidden;
    background: var(--black);
  }
  .poster {
    position: relative;
    width: 1200px;
    height: 520px;
    background: var(--black);
    color: var(--gold);
    font-family: "Bitter", Georgia, serif;
  }
  .frame {
    position: absolute;
    inset: 0;
  }
  .title {
    position: absolute;
    left: 0;
    top: 96px;
    width: 1200px;
    height: 80px;
  }
  .title text {
    font-family: "Limelight", "Federo", sans-serif;
    font-size: 84px;
  }
  .rule {
    position: absolute;
    height: 5px;
    background: var(--gold-light);
  }
  .rule--title { left: 174px; width: 849px; top: 175px; }
  .rule--info { left: 257px; width: 685px; top: 307px; }
  .motto, .slogan, .details, .dj, .dresscode, .dresscode-men {
    position: absolute;
    left: 0;
    width: 1200px;
    margin: 0;
    text-align: center;
    font-weight: 400;
  }
  .motto { top: 184px; font-size: 45px; line-height: 56px; color: var(--gold); }
  .slogan { top: 243px; font-size: 38px; line-height: 48px; color: var(--gold); }
  .details { top: 316px; font-size: 36px; line-height: 48px; color: var(--gold); }
  .dj { top: 364px; font-size: 34px; line-height: 44px; color: var(--gold-light); }
  .dresscode { top: 410px; font-size: 18px; line-height: 22px; color: var(--gold); }
  .dresscode-men { top: 430px; font-size: 18px; line-height: 22px; color: var(--gold); }
  .club {
    position: absolute;
    left: 128px;
    top: 274px;
    width: 114px;
    height: 114px;
    border: 2px solid var(--gold);
    border-radius: 50%;
    box-sizing: border-box;
    display: flex;
    align-items: center;
    justify-content: center;
    text-align: center;
  }
  .club__name {
    font-family: "Bitter", Georgia, serif;
    font-weight: 500;
    font-size: 11px;
    line-height: 14px;
    color: var(--gold);
    letter-spacing: 0.5px;
  }
</style>
</head>
<body>
<main class="poster">

  <svg class="frame" width="1200" height="520" viewBox="0 0 1200 520" aria-hidden="true">
    <defs>
      <radialGradient id="ornamentGlow" cx="50%" cy="50%" r="50%">
        <stop offset="0%" stop-color="#c9a860" stop-opacity="0.45"/>
        <stop offset="100%" stop-color="#c9a860" stop-opacity="0"/>
      </radialGradient>
    </defs>
    <g fill="none" stroke="#c9a860" stroke-width="2">
      <rect class="frame__outer" x="27" y="28" width="1146" height="463"/>
      <rect class="frame__inner" x="50" y="50" width="1100" height="419"/>
      <line x1="66" y1="40" x2="1134" y2="40"/>
      <line x1="66" y1="480" x2="1134" y2="480"/>
      <line x1="38" y1="66" x2="38" y2="454"/>
      <line x1="1162" y1="66" x2="1162" y2="454"/>
      <line x1="174" y1="83" x2="1023" y2="83"/>
      <line x1="408" y1="76" x2="789" y2="76"/>
      <line x1="56" y1="150" x2="56" y2="370"/>
      <line x1="1144" y1="150" x2="1144" y2="370"/>
    </g>
    <path role="img" aria-label="Art-déco-Fächer über dem Titel" d="M536 83 A62 62 0 0 1 660 83 Z" fill="url(#ornamentGlow)"/>
    <path role="img" aria-label="Art-déco-Raute am unteren Rand" d="M600 462 L622 480 L600 498 L578 480 Z" fill="url(#ornamentGlow)"/>
    <rect role="img" aria-label="Fächerornament oben links" x="50" y="50" width="54" height="54" fill="url(#ornamentGlow)"/>
    <rect role="img" aria-label="Fächerornament oben rechts" x="1096" y="50" width="54" height="54" fill="url(#ornamentGlow)"/>
    <rect role="img" aria-label="Fächerornament unten links" x="50" y="415" width="54" height="54" fill="url(#ornamentGlow)"/>
    <rect role="img" aria-label="Fächerornament unten rechts" x="1096" y="415" width="54" height="54" fill="url(#ornamentGlow)"/>
    <ellipse role="img" aria-label="Strahlenornament links" cx="70" cy="260" rx="62" ry="90" fill="url(#ornamentGlow)"/>
    <ellipse role="img" aria-label="Strahlenornament rechts" cx="1130" cy="260" rx="62" ry="90" fill="url(#ornamentGlow)"/>
  </svg>

  <svg class="title" width="1200" height="80" viewBox="0 0 1200 80">
    <defs>
      <linearGradient id="titleGold" x1="0" y1="0" x2="1" y2="0">
        <stop offset="0%" stop-color="#b8975a"/>
        <stop offset="35%" stop-color="#f2d68a"/>
        <stop offset="65%" stop-color="#e8c877"/>
        <stop offset="100%" stop-color="#b8975a"/>
      </linearGradient>
    </defs>
    <text x="118" y="67" textLength="964" lengthAdjust="spacingAndGlyphs" fill="url(#titleGold)">DIE PARTY DER GOLDENEN 20ER</text>
  </svg>

  <div class="rule rule--title"></div>

  <h2 class="motto">Glanz · Glamour · Lebenslust</h2>
  <p class="slogan">Tanzen wie früher – Feiern wie nie</p>

  <div class="rule rule--info"></div>

  <p class="details">21. März / 20.30 Uhr / Saal KM</p>
  <p class="dj">LifeDJ - Marlies</p>
  <p class="dresscode">Dresscode: Goldene 20er. Frauen: Fransen, Federn, Hosenträger, Zylinder.</p>
  <p class="dresscode-men">Männer: Anzug, Fliege, Hut</p>

  <div class="club">
    <span class="club__name">Hinterkalmbacher<br>Heimatpflege&shy;verein</span>
  </div>

</main>
</body>
</html>
```